Lanterns Across a Copper Orchard Book Cover

Need a book cover that jumps out, simple is good. I am trying to relay to readers that they face a serious tax burden when they reach retirement.

I am attaching the cover I've been using, which I designed, but it's not nearly effective enough.
Get rid of the word "Accounts" in the cover, please.

```html
<!DOCTYPE html>
<html lang="en">
<head>
<meta charset="utf-8">
<title>Lanterns Across a Copper Orchard – Book Cover</title>
<link rel="stylesheet" href="https://fonts.googleapis.com/css2?family=Playfair+Display:wght@900&family=Libre+Baskerville:wght@700&family=Montserrat:wght@600&family=Open+Sans:wght@400;600;700&display=swap">
<style>
  :root {
    --navy: #07334a;
    --gold: #c09455;
    --teal: #3aa3c4;
    --teal-light: #6fc6de;
    --cover-bg: #dde3ee;
    --cover-glow: #f5f7fb;
    --subtitle-grey: #9a9a9c;
    --rule: #9aa5b5;
    --white: #ffffff;
  }
  * { margin: 0; padding: 0; box-sizing: border-box; }
  html, body { width: 1200px; height: 960px; overflow: hidden; background: var(--white); }
  .canvas { position: relative; width: 1200px; height: 960px; font-family: "Open Sans", sans-serif; }

  /* Back cover */
  .back-cover { position: absolute; left: 78px; top: 54px; width: 531px; height: 844px; background: var(--navy); }
  .brand { position: absolute; left: 158px; top: 77px; display: flex; align-items: center; gap: 6px; color: var(--teal-light); font-size: 13px; font-weight: 600; letter-spacing: 0.5px; }
  .brand-dot { width: 14px; height: 14px; border-radius: 50%; background: var(--teal); }
  .benefit { position: absolute; display: flex; align-items: center; gap: 9px; color: var(--teal); font-size: 10.5px; font-weight: 600; line-height: 1.3; }
  .benefit svg { flex: none; }
  .benefit b { font-weight: 700; }
  .website { position: absolute; left: 0; width: 100%; top: 257px; text-align: center; color: #b8c3cc; font-family: "Libre Baskerville", serif; font-weight: 400; font-size: 10px; letter-spacing: 6.2px; }
  .divider { position: absolute; left: 73px; top: 308px; width: 400px; height: 1px; background: var(--teal); }
  .bio-heading { position: absolute; left: 73px; top: 342px; color: var(--white); font-size: 10.5px; font-weight: 700; line-height: 14.5px; }
  .bio-heading .name { font-size: 14px; letter-spacing: 0.3px; }
  .bio-heading .accent { color: var(--teal-light); }
  .author-photo { position: absolute; left: 73px; top: 414px; width: 174px; height: 242px; background: linear-gradient(160deg, #6a5a55 0%, #8d8a86 40%, #5b5f63 100%); }
  .bio-text { position: absolute; left: 269px; width: 215px; color: var(--white); font-size: 11.6px; line-height: 19.2px; }
  .bio-text strong { font-weight: 600; }
  .bio-one { top: 410px; }
  .bio-two { top: 562px; }
  .isbn-box { position: absolute; left: 326px; top: 714px; width: 182px; height: 110px; background: var(--white); }

  /* Front cover */
  .front-cover { position: absolute; left: 609px; top: 54px; width: 529px; height: 842px; overflow: hidden;
    background: radial-gradient(ellipse 60% 55% at 75% 45%, var(--cover-glow) 0%, var(--cover-bg) 75%);
    box-shadow: 2px 2px 4px rgba(0,0,0,0.25); }
  .corner-flag { position: absolute; left: 0; top: 0; }
  .hourglass { position: absolute; left: 271px; top: 78px; width: 200px; height: 444px;
    background: radial-gradient(ellipse 45% 22% at 50% 28%, #d9c7a6 0%, rgba(230,232,238,0.6) 70%, transparent 100%),
                radial-gradient(ellipse 48% 22% at 50% 78%, #e0cfae 0%, rgba(230,232,238,0.6) 70%, transparent 100%);
    border-radius: 45% 45% 45% 45% / 25% 25% 25% 25%; }
  .title { position: absolute; left: 51px; font-family: "Playfair Display", serif; font-weight: 900; line-height: 1; transform: scaleX(0.78); transform-origin: left top; white-space: nowrap; letter-spacing: -1px; }
  .title-navy { color: var(--navy); }
  .title-gold { color: var(--gold); }
  .t1 { top: 222px; font-size: 74px; }
  .t2 { top: 286px; font-size: 96px; }
  .t3 { top: 372px; font-size: 120px; }
  .t4 { top: 486px; font-size: 104px; }
  .subtitle { position: absolute; left: 56px; top: 632px; color: var(--subtitle-grey); font-family: "Libre Baskerville", serif; font-weight: 700; font-size: 20px; line-height: 27px; letter-spacing: 0.3px; }
  .author-rule { position: absolute; left: 46px; width: 435px; height: 1px; background: var(--rule); }
  .rule-top { top: 720px; }
  .rule-bottom { top: 788px; }
  .author-name { position: absolute; left: 46px; width: 435px; top: 726px; text-align: center; color: var(--gold); font-family: "Montserrat", sans-serif; font-weight: 600; font-size: 44px; line-height: 56px; letter-spacing: 1px; }
</style>
</head>
<body>
<div class="canvas">

  <section class="back-cover">
    <div class="brand"><span class="brand-dot"></span>Northfield Wealth Planning</div>

    <div class="benefit" style="left:80px; top:160px;">
      <svg width="30" height="30" viewBox="0 0 30 30"><circle cx="15" cy="15" r="13.5" fill="none" stroke="#fff" stroke-width="2"/><rect x="9" y="11" width="12" height="9" rx="1" fill="none" stroke="#fff" stroke-width="1.5"/><text x="15" y="18.5" font-size="7" fill="#fff" text-anchor="middle" font-family="sans-serif">$</text></svg>
      <span><b>REDUCE</b> income tax</span>
    </div>
    <div class="benefit" style="left:269px; top:160px;">
      <svg width="30" height="30" viewBox="0 0 30 30"><circle cx="15" cy="15" r="13.5" fill="none" stroke="#fff" stroke-width="2"/><path d="M8 15 L15 9 L22 15 M10 14 V21 H20 V14" fill="none" stroke="#fff" stroke-width="1.5"/></svg>
      <span><b>ELIMINATE</b> social security tax</span>
    </div>
    <div class="benefit" style="left:80px; top:206px;">
      <svg width="30" height="30" viewBox="0 0 30 30"><circle cx="15" cy="15" r="13.5" fill="none" stroke="#fff" stroke-width="2"/><path d="M12 8 H18 V12 H22 V18 H18 V22 H12 V18 H8 V12 H12 Z" fill="#fff"/></svg>
      <span><b>AVOID</b> huge Medicare<br>premium increases</span>
    </div>
    <div class="benefit" style="left:269px; top:206px;">
      <svg width="30" height="30" viewBox="0 0 30 30"><circle cx="15" cy="15" r="13.5" fill="none" stroke="#fff" stroke-width="2"/><rect x="9" y="16" width="3" height="5" fill="#fff"/><rect x="13.5" y="13" width="3" height="8" fill="#fff"/><rect x="18" y="10" width="3" height="11" fill="#fff"/></svg>
      <span><b>LEAVE</b> a tax-free legacy</span>
    </div>

    <div class="website">www.northfieldwealthplanning.com</div>
    <div class="divider"></div>

    <div class="bio-heading">
      <span class="name">DANIEL MARLOWE</span> is<br>
      <span class="accent">a CERTIFIED FINANCIAL PLANNER</span><br>
      and holds <span class="accent">a Master’s degree in</span><br>
      <span class="accent">Personal Financial Planning</span>
    </div>

    <div class="author-photo" role="img" aria-label="Portrait photograph of the author in a grey suit"></div>

    <p class="bio-text bio-one">Daniel has provided financial advice to clients since 1998. Over those 2 decades he has developed extensive knowledge of <strong>Investment Management, SOCIAL SECURITY, Tax, Retirement Planning and wealth transfer strategies.</strong></p>
    <p class="bio-text bio-two">He has learned that successful financial planning does not need to be complex. He follows the tried and true rule he learned in the Army, “Keep It Simple.”</p>

    <div class="isbn-box"></div>
  </section>

  <section class="front-cover">
    <svg class="corner-flag" width="150" height="112" viewBox="0 0 150 112"><polygon points="0,0 150,0 0,112" fill="var(--gold)"/></svg>

    <div class="hourglass" role="img" aria-label="Glass hourglass with sand and a sculpted dollar sign falling into the word TAX"></div>

    <h1>
      <span class="title title-navy t1">LANTERNS</span>
      <span class="title title-gold t2">ACROSS A</span>
      <span class="title title-gold t3">COPPER</span>
      <span class="title title-navy t4">ORCHARD</span>
    </h1>

    <p class="subtitle">HOW THE ROTH IRA<br>CAN HELP YOU AVOID IT</p>

    <div class="author-rule rule-top"></div>
    <p class="author-name">DANIEL MARLOWE</p>
    <div class="author-rule rule-bottom"></div>
  </section>

</div>
</body>
</html>
```